Spiritual journeyer, astrologer, Reiki master, underground music lover needs business card design

Initially I need a business card design (and possibly a logo for my new website). I offer astrological and energetic inquiry and guidance to clients in support of their life's evolutionary path. I combine an eclectic mix of methods with a focus on the mind body connection. I am a spiritual journeyer, astrologer, Reiki Master, certified personal trainer, soon to be black belt in Taekwondo (karate), and researcher into the benefits of music/sound vibrational therapy. And underground music lover :) The attached drawing is just something I drew freehand, it is symbolic of many things important to me. I wanted the figure to clearly be female. Her arms are open to catch the sky, the name of my new business is Noraweaver, and Nora is my daughter's name. This was just an idea I had, I'm open to suggestions. The photo is me with the planets in the sky as they were at the moment I was born (some years ago-LOL)

I have picked a final design. Thank you everyone for your time and effort.

Target Market(s)

Worldwide, what I do can be done in person or anywhere in the world via Skype

Industry/Entity Type

Professional Service

Contact Information for Business Card

Simple, unusual image with my business name and contact info

Font styles to use
Sans Serif

Requirements
Must have
• My website very clean, simple. Somehow combine biz name of Noraweaver with female figure catching/holding the starry sky? See my poor drawing I attached.
Nice to have
• Something that conveys all the unique, unusual, eclectic skills and capacities I have
Should not have
• Frilly, fancy, stuffy

```html
<!DOCTYPE html>
<html lang="en">
<head>
<meta charset="utf-8">
<title>Noraweaver business card</title>
<link rel="stylesheet" href="https://fonts.googleapis.com/css2?family=Exo+2:wght@400;500;600&display=swap">
<style>
  :root {
    --backdrop: #d0d0d0;
    --brand-blue: #233f8c;
    --card-white: #ffffff;
    --flame-orange: #ff8a00;
    --flame-red: #ff3d00;
    --ink: #2b2b2b;
    --on-dark: #ffffff;
  }
  * { margin: 0; padding: 0; box-sizing: border-box; }
  html, body { width: 1200px; height: 900px; overflow: hidden; }
  body {
    position: relative;
    background: var(--backdrop);
    font-family: "Exo 2", sans-serif;
  }
  .card { position: absolute; overflow: hidden; }

  /* Front */
  .card-front { left: 76px; top: 59px; width: 533px; height: 345px; background: var(--card-white); }
  .front-panel { position: absolute; inset: 0; }
  .brand {
    position: absolute; display: flex; align-items: center; gap: 10px;
    color: var(--on-dark); font-weight: 500; font-size: 19px; letter-spacing: 0.2px;
  }
  .brand-dot { width: 18px; height: 18px; border-radius: 50%; background: var(--flame-orange); }
  .card-front .brand { left: 88px; top: 181px; }
  .name-ribbon { position: absolute; left: 277px; top: 81px; width: 256px; height: 80px; }
  .name-ribbon .name {
    position: absolute; left: 0; top: 0; width: 256px; height: 46px;
    display: flex; align-items: center; justify-content: center;
    color: var(--on-dark); font-size: 25px; font-weight: 500;
  }
  .card-front .service {
    position: absolute; left: 320px; top: 135px; width: 200px;
    text-align: center; color: var(--ink); font-size: 17px; line-height: 21px;
  }
  .contacts { position: absolute; list-style: none; }
  .contacts li { display: flex; align-items: center; gap: 6px; height: 23px; font-size: 15px; }
  .contacts svg { width: 13px; height: 13px; flex: none; }
  .card-front .contacts { left: 322px; top: 230px; color: var(--ink); }

  /* Back */
  .card-back { left: 556px; top: 458px; width: 564px; height: 366px; }
  .back-photo {
    position: absolute; inset: 0;
    background:
      radial-gradient(ellipse 170px 190px at 410px 150px, rgba(255,214,170,0.95), rgba(255,120,40,0.55) 45%, rgba(0,0,0,0) 100%),
      radial-gradient(ellipse 260px 230px at 470px 90px, rgba(200,70,40,0.7), rgba(0,0,0,0) 100%),
      radial-gradient(ellipse 220px 200px at 300px 60px, rgba(120,90,140,0.55), rgba(0,0,0,0) 100%),
      linear-gradient(90deg, #0d0d10 0%, #141217 40%, #3a2a2a 70%, #5a3a20 100%);
  }
  .card-back .brand { left: 60px; top: 76px; font-size: 13px; gap: 8px; }
  .card-back .brand-dot { width: 14px; height: 14px; }
  .card-back .name {
    position: absolute; left: 54px; top: 130px;
    color: var(--on-dark); font-size: 26px; font-weight: 500;
  }
  .card-back .service {
    position: absolute; left: 55px; top: 174px;
    color: var(--on-dark); font-size: 18px; line-height: 22.5px;
  }
  .card-back .contacts { left: 57px; top: 252px; color: var(--on-dark); }
  .card-back .contacts li { height: 24px; gap: 3px; }
</style>
</head>
<body>

  <section class="card card-front">
    <svg class="front-panel" viewBox="0 0 533 345" aria-hidden="true">
      <polygon points="0,0 381,0 241,345 0,345" fill="var(--brand-blue)"/>
    </svg>
    <div class="brand"><span class="brand-dot"></span>NORAWEAVER</div>
    <div class="name-ribbon">
      <svg width="256" height="80" viewBox="0 0 256 80" aria-hidden="true">
        <defs>
          <linearGradient id="ribbonFill" x1="0" x2="1" y1="0" y2="0">
            <stop offset="0" stop-color="var(--flame-orange)"/>
            <stop offset="1" stop-color="var(--flame-red)"/>
          </linearGradient>
        </defs>
        <polygon points="0,46 37,46 37,80" fill="#d94d00"/>
        <rect x="0" y="0" width="256" height="46" fill="url(#ribbonFill)"/>
      </svg>
      <div class="name">Miriam Hale</div>
    </div>
    <p class="service">Austrological and Energetic Guidence and Inquiry</p>
    <ul class="contacts">
      <li><svg viewBox="0 0 14 14"><circle cx="7" cy="7" r="6" fill="none" stroke="currentColor" stroke-width="1.2"/><ellipse cx="7" cy="7" rx="2.6" ry="6" fill="none" stroke="currentColor" stroke-width="1"/><line x1="1" y1="7" x2="13" y2="7" stroke="currentColor" stroke-width="1"/></svg>www.noraweaver.com</li>
      <li><svg viewBox="0 0 14 14"><rect x="1" y="3" width="12" height="8" fill="currentColor"/><polyline points="1,3 7,8 13,3" fill="none" stroke="#fff" stroke-width="1"/></svg>emailnoraweaver</li>
      <li><svg viewBox="0 0 14 14"><circle cx="7" cy="7" r="6" fill="none" stroke="currentColor" stroke-width="1.1"/><path d="M4.6 4 l1.3-.4 .8 1.7-.8.7 a4 4 0 0 0 2 2 l.7-.8 1.7.8-.4 1.3 c-2.8.3-5.6-2.5-5.3-5.3z" fill="currentColor"/></svg>555-210-4873</li>
    </ul>
  </section>

  <section class="card card-back">
    <div class="back-photo" role="img" aria-label="Photograph of a woman in silhouette with arms raised against a burst of warm light and dark starry colours"></div>
    <div class="brand"><span class="brand-dot"></span>NORAWEAVER</div>
    <div class="name">Miriam Hale</div>
    <p class="service">Austrological and<br>Energetic Guidence<br>and Inquiry</p>
    <ul class="contacts">
      <li><svg viewBox="0 0 14 14"><circle cx="7" cy="7" r="6" fill="none" stroke="currentColor" stroke-width="1.2"/><ellipse cx="7" cy="7" rx="2.6" ry="6" fill="none" stroke="currentColor" stroke-width="1"/><line x1="1" y1="7" x2="13" y2="7" stroke="currentColor" stroke-width="1"/></svg>www.noraweaver.com</li>
      <li><svg viewBox="0 0 14 14"><rect x="1" y="3" width="12" height="8" fill="currentColor"/><polyline points="1,3 7,8 13,3" fill="none" stroke="#111" stroke-width="1"/></svg>emailnoraweaver</li>
      <li><svg viewBox="0 0 14 14"><path d="M3.5 2.5 l2-.6 1.2 2.6-1.2 1 a6 6 0 0 0 3 3 l1-1.2 2.6 1.2-.6 2 c-4.2.5-8.5-3.8-8-8z" fill="currentColor"/></svg>555-210-4873</li>
    </ul>
  </section>

</body>
</html>
```